New Look and Feel for 82 year old Varnstedt Ltd. presentations

We are seeking new ideas to have powerpoint-layouts for the group headquarters. Varnstedt is an industrial company in maritime, hydraulics, heavy machinery and industrial services. Please read our history and watch the video for a quick familiarization. http://www.varnstedt-example.fi/eng/main.php

Our customer relationships are based on trust, with Varnstedt providing to customers, cooperation partners and other interest groups products and solutions that produce sustainable benefits.

Varnstedt strives to ensure that the environmental impact of the products is considered over the entire life cycle and the processes used by the Group are as environmentally benign as possible.

Colors

Designer to choose colors to be used in the design.

Requirements
Must have
• Logo
Nice to have
• example animations and transitions

```html
<!DOCTYPE html>
<html lang="en">
<head>
<meta charset="UTF-8">
<title>Varnstedt – Presentation Title Slide</title>
<link href="https://fonts.googleapis.com/css2?family=Lato:wght@400;700;900&display=swap" rel="stylesheet">
<style>
  :root {
    --brand-red: #f2524b;
    --title-red: #e8473f;
    --ink: #333333;
    --paper: #ffffff;
    --photo-dark: #0b0b0c;
    --photo-mid: #3a3f48;
    --photo-light: #c9c9c6;
  }
  html, body {
    margin: 0;
    padding: 0;
    width: 1200px;
    height: 900px;
    overflow: hidden;
    background: var(--paper);
  }
  .slide {
    position: relative;
    width: 1200px;
    height: 900px;
    background: var(--paper);
    font-family: "Lato", Arial, sans-serif;
    overflow: hidden;
  }
  .slide-shapes {
    position: absolute;
    inset: 0;
    width: 1200px;
    height: 900px;
  }
  .title-block {
    position: absolute;
    left: 99px;
    top: 462px;
  }
  .project-title {
    margin: 0;
    font-size: 37px;
    font-weight: 700;
    color: var(--title-red);
    line-height: 1.1;
  }
  .project-subtext {
    margin: 10px 0 0;
    font-size: 27px;
    font-weight: 400;
    color: var(--ink);
  }
  .brand {
    position: absolute;
    left: 108px;
    top: 740px;
    display: flex;
    align-items: center;
    gap: 20px;
  }
  .brand-square {
    width: 46px;
    height: 46px;
    background: var(--brand-red);
  }
  .brand-name {
    font-size: 64px;
    font-weight: 900;
    color: var(--ink);
    line-height: 1;
  }
</style>
</head>
<body>
  <main class="slide">
    <svg class="slide-shapes" viewBox="0 0 1200 900" xmlns="http://www.w3.org/2000/svg">
      <defs>
        <linearGradient id="photoTone" x1="0" y1="0" x2="1" y2="1">
          <stop offset="0" stop-color="var(--photo-dark)"/>
          <stop offset="0.45" stop-color="var(--photo-mid)"/>
          <stop offset="1" stop-color="var(--photo-light)"/>
        </linearGradient>
      </defs>
      <polygon class="accent-band" points="446,75 474,75 668,900 645,900" fill="var(--brand-red)"/>
      <polygon class="hero-photo" role="img"
        aria-label="Photo: technician in cap and blue overalls servicing a large toothed slewing ring inside heavy machinery, sparks in the background"
        points="458,0 1200,0 1200,900 668,900" fill="url(#photoTone)"/>
    </svg>

    <section class="title-block">
      <h1 class="project-title">Project Title Here</h1>
      <p class="project-subtext">Subtext here</p>
    </section>

    <div class="brand">
      <span class="brand-square"></span>
      <span class="brand-name">Varnstedt</span>
    </div>
  </main>
</body>
</html>
```